Business Card Professional Clean - Ledgerpeak

Create a business card for my company that deals with Cryptocurrencies. I have a few designs ideas that I'd like to be implemented. Thanks! I will include the logo files, and a link to the design styles that I like.

Target Market(s)

Professionals

Industry/Entity Type

Consulting

Contact Information for Business Card

Name: Mark Dunn
Title: CEO/Technical Director
Phone: (587)430-9158
E-mail: mdunn@ledgerpeak.example
Address: Suite 512, 208-3375 Harwood Lane NW

Twitter: @LedgerPeakYYC
Instagram: ledgerpeakyyc

Colors
92b5d7
3276b5
33a6d7
85acd3
85cae6
0592cd

Requirements
Must have
• Some colors that match with the logo and the pictures I put in below.
• Ideally the finished product would look something like the attachments showing the color gradient I want.
Nice to have
• Please see some of the attachments I've included. This is very close to the final product that I would like to see. If someone could recreate something like those I would definitely feel pretty good about it.
• For the instagram and twitter please use the symbols/icon to represent it on the card.
Should not have
• No crazy colors and unprofessional styles. I just want clear info. Don't go outside the boundaries of the colors in the attachment and we should be good. No crazy weird fonts either.

```html
<!DOCTYPE html>
<html lang="en">
<head>
<meta charset="utf-8">
<title>Ledgerpeak Business Card</title>
<link rel="stylesheet" href="https://fonts.googleapis.com/css2?family=Open+Sans:wght@300;400;600;700&display=swap">
<style>
  :root {
    --stage: #e4e6e9;
    --paper: #ffffff;
    --navy: #3d4b5f;
    --ink: #2b303a;
    --ink-soft: #5a6070;
    --brand: #3276b5;
    --blue-1: #3276b5;
    --blue-2: #0592cd;
    --blue-3: #33a6d7;
    --blue-4: #85acd3;
    --blue-5: #92b5d7;
    --blue-6: #85cae6;
    --on-navy: #f2f4f7;
  }
  * { box-sizing: border-box; margin: 0; padding: 0; }
  html, body { width: 1200px; height: 873px; overflow: hidden; }
  body {
    background: var(--stage);
    font-family: "Open Sans", Arial, sans-serif;
    display: flex;
    align-items: center;
    justify-content: center;
    gap: 60px;
  }
  .card {
    position: relative;
    width: 520px;
    height: 298px;
    border-radius: 4px;
    box-shadow: 0 10px 28px rgba(30, 40, 55, 0.18);
    overflow: hidden;
  }

  /* Front */
  .card--front { background: var(--paper); color: var(--ink); }
  .contact { position: absolute; left: 36px; top: 36px; }
  .contact__name { font-size: 22px; font-weight: 700; letter-spacing: 0.3px; }
  .contact__title { font-size: 11px; color: var(--ink-soft); margin-top: 4px; }
  .contact__line { font-size: 11.5px; color: var(--ink-soft); margin-top: 10px; letter-spacing: 0.6px; }
  .contact__line + .contact__line { margin-top: 4px; }
  .address {
    position: absolute; left: 36px; bottom: 30px;
    font-size: 11.5px; letter-spacing: 1.8px; color: var(--ink);
  }
  .gradient-bar {
    position: absolute; display: flex; flex-direction: column;
  }
  .gradient-bar span { flex: 1; }
  .gradient-bar span:nth-child(1) { background: var(--blue-6); }
  .gradient-bar span:nth-child(2) { background: var(--blue-3); }
  .gradient-bar span:nth-child(3) { background: var(--blue-2); }
  .gradient-bar span:nth-child(4) { background: var(--blue-1); }
  .gradient-bar--divider { left: 262px; top: 34px; width: 13px; height: 172px; }
  .gradient-bar--tab { right: 0; top: 196px; width: 13px; height: 70px; flex-direction: column-reverse; }
  .brand {
    position: absolute; display: flex; align-items: center; gap: 10px;
  }
  .brand--front { left: 300px; top: 104px; color: var(--brand); }
  .brand__name { font-size: 23px; font-weight: 400; letter-spacing: 2.5px; text-transform: uppercase; }
  .brand__square { width: 14px; height: 14px; background: currentColor; }

  /* Back */
  .card--back { background: var(--navy); color: var(--on-navy); }
  .brand--back { left: 50%; top: 50%; transform: translate(-50%, -50%); }
  .brand--back .brand__name { font-size: 32px; font-weight: 300; letter-spacing: 4px; }
  .brand--back .brand__square { width: 18px; height: 18px; background: none; border: 1.5px solid currentColor; }
  .social {
    position: absolute; display: flex; align-items: center; gap: 7px;
    font-size: 10.5px; letter-spacing: 0.6px;
  }
  .social svg { width: 12px; height: 12px; }
  .social--twitter { left: 30px; top: 26px; }
  .social--instagram { right: 30px; bottom: 26px; }
</style>
</head>
<body>
  <section class="card card--front" aria-label="Business card front">
    <div class="contact">
      <p class="contact__name">Mark Dunn</p>
      <p class="contact__title">CEO | Technical Director</p>
      <p class="contact__line">(587) 430 - 9158</p>
      <p class="contact__line">mdunn@ledgerpeak.example</p>
    </div>
    <div class="gradient-bar gradient-bar--divider"><span></span><span></span><span></span><span></span></div>
    <div class="brand brand--front">
      <span class="brand__name">Ledgerpeak</span>
      <span class="brand__square"></span>
    </div>
    <p class="address">Suite 512,&nbsp;&nbsp; 208-3375 Harwood Lane&nbsp;&nbsp; NW</p>
    <div class="gradient-bar gradient-bar--tab"><span></span><span></span><span></span><span></span></div>
  </section>

  <section class="card card--back" aria-label="Business card back">
    <p class="social social--twitter">
      <svg viewBox="0 0 12 12" aria-hidden="true"><circle cx="6" cy="6" r="5.2" fill="none" stroke="currentColor" stroke-width="1"/></svg>
      @LedgerPeakYYC
    </p>
    <div class="brand brand--back">
      <span class="brand__name">Ledgerpeak</span>
      <span class="brand__square"></span>
    </div>
    <p class="social social--instagram">
      <svg viewBox="0 0 12 12" aria-hidden="true"><circle cx="6" cy="6" r="5.2" fill="none" stroke="currentColor" stroke-width="1"/></svg>
      ledgerpeakyyc
    </p>
  </section>
</body>
</html>
```